Property risk and finance brokerage company needs a business card design

Tarlow Financial requires a business card design. Please integrate existing logo (refer uploaded file).
hex codes used on logo #002649 #008ED6 #444F51 #ADAFAA
font used - Cinzel
Contact information
Renata Sollisford
Director
Mobile: 0491 738 205
email: r.sollisford@tarlowfinancial.example.au
website: www.tarlowfinancial.example.au
CRN : 918354
PO Box 527
Brindlewood, Victoria, 3189
Horizontal orientation please
Finance

```html
<!DOCTYPE html>
<html lang="en">
<head>
<meta charset="utf-8">
<title>Tarlow Financial – Business Card</title>
<link rel="stylesheet" href="https://fonts.googleapis.com/css2?family=Signika:wght@300;400&display=swap">
<style>
  :root {
    --page: #ffffff;
    --card: #ffffff;
    --ink: #555a5e;
    --blue-top: #1b7db8;
    --blue-mid: #1f5d8a;
    --navy: #253247;
    --brand: #1d5f90;
    --white: #ffffff;
    --shadow: rgba(0, 0, 0, 0.35);
  }
  * { margin: 0; padding: 0; box-sizing: border-box; }
  html, body {
    width: 973px; height: 1200px; overflow: hidden;
    background: var(--page);
    font-family: "Signika", "Segoe UI", sans-serif;
    font-weight: 300;
  }
  .canvas { position: relative; width: 973px; height: 1200px; }

  .card {
    position: absolute; left: 15px; width: 943px; height: 568px;
    border-radius: 22px;
    box-shadow: 0 2px 6px var(--shadow);
    overflow: hidden;
  }
  .card--front { top: 15px; background: var(--card); }
  .card--back {
    top: 615px;
    background: linear-gradient(to bottom, var(--blue-top) 0%, var(--blue-mid) 45%, var(--navy) 100%);
  }

  .text-block { position: absolute; right: 41px; text-align: right; color: var(--ink); font-size: 27px; line-height: 37px; }
  .postal { top: 40px; }
  .contact { top: 433px; }

  .band {
    position: absolute; top: 212px; height: 146px;
    background: linear-gradient(to bottom, var(--blue-top) 0%, var(--blue-mid) 50%, var(--navy) 100%);
  }
  .band--left { left: 0; width: 33px; border-radius: 0 6px 6px 0; }
  .band--right { left: 406px; right: 0; border-radius: 8px 0 0 8px; }
  .person { position: absolute; right: 41px; top: 26px; text-align: right; color: var(--white); }
  .person__name { font-size: 38px; line-height: 46px; font-weight: 300; }
  .person__role { font-size: 27px; line-height: 36px; font-weight: 300; margin-top: 4px; }

  .brand {
    position: absolute; display: flex; align-items: center;
    font-weight: 400;
  }
  .brand--front { left: 50px; top: 212px; height: 146px; color: var(--brand); font-size: 36px; gap: 14px; }
  .brand--back { left: 0; right: 0; top: 170px; height: 230px; justify-content: center; color: var(--white); font-size: 64px; gap: 24px; }
  .brand__dot { border-radius: 50%; background: currentColor; flex: none; }
  .brand--front .brand__dot { width: 40px; height: 40px; }
  .brand--back .brand__dot { width: 70px; height: 70px; }

  .tab { position: absolute; top: 211px; width: 35px; height: 145px; background: var(--white); }
  .tab--left { left: 0; border-radius: 0 8px 8px 0; }
  .tab--right { right: 0; border-radius: 8px 0 0 8px; }

  .back-address {
    position: absolute; left: 0; right: 0; top: 510px;
    text-align: center; color: var(--white); font-size: 22px;
  }
</style>
</head>
<body>
<div class="canvas">
  <section class="card card--front">
    <div class="text-block postal">
      <p>PO Box 527</p>
      <p>Brindlewood, Victoria, 3189</p>
    </div>

    <div class="band band--left"></div>
    <div class="brand brand--front">
      <span class="brand__dot"></span>
      <span class="brand__name">Tarlow Financial</span>
    </div>
    <div class="band band--right">
      <div class="person">
        <p class="person__name">Renata Sollisford</p>
        <p class="person__role">Managing Director</p>
      </div>
    </div>

    <div class="text-block contact">
      <p>Mobile: 0491 738 205</p>
      <p>email: r.sollisford@tarlowfinancial.example.au</p>
      <p>Credit Rep No.: nnn nnn nnn</p>
    </div>
  </section>

  <section class="card card--back">
    <div class="tab tab--left"></div>
    <div class="tab tab--right"></div>
    <div class="brand brand--back">
      <span class="brand__dot"></span>
      <span class="brand__name">Tarlow Financial</span>
    </div>
    <p class="back-address">PO Box 527, Brindlewood, Victoria, 3189</p>
  </section>
</div>
</body>
</html>
```